Corrindale Planners, LLC Stationary

Corrindale Planners, LLC is a new financial planning and consulting company. We are looking for designs on business cards, letterhead, envelopes, and anything else that would be useful. Our preference for business card design is two sided. We are looking for a professional and clean look with incorporating the logo and patriotic feel. Thank you to all who participate and good luck!

```html
<!DOCTYPE html>
<html lang="en">
<head>
<meta charset="utf-8">
<title>Corrindale Planners, LLC Stationery</title>
<link href="https://fonts.googleapis.com/css2?family=Questrial&display=swap" rel="stylesheet">
<style>
  :root {
    --navy: #143d68;
    --navy-deep: #10375f;
    --red: #c0232b;
    --paper: #f2f2f2;
    --backdrop: #d0d0d0;
    --ink: #3a3a3a;
    --muted: #5a5a5a;
  }
  * { box-sizing: border-box; margin: 0; padding: 0; }
  html, body { width: 1200px; height: 1041px; overflow: hidden; }
  body {
    background: var(--backdrop);
    font-family: "Questrial", "Century Gothic", sans-serif;
    color: var(--ink);
    position: relative;
  }
  .piece { position: absolute; box-shadow: 0 1px 3px rgba(0,0,0,.18); }

  /* brand lockup */
  .brand { display: flex; align-items: center; gap: 6px; }
  .brand-mark { width: 14px; height: 14px; background: var(--red); flex: none; }
  .brand-text { display: flex; flex-direction: column; }
  .brand-name { color: var(--navy); letter-spacing: .04em; line-height: 1; text-transform: uppercase; }
  .brand-tag { color: var(--navy); text-transform: uppercase; letter-spacing: .12em; margin-top: 3px; line-height: 1; }
  .on-dark .brand-name, .on-dark .brand-tag { color: #ffffff; }

  /* presentation folder */
  .folder { left: 166px; top: 76px; width: 418px; height: 541px; background: var(--navy); border-radius: 3px; }
  .folder-spine { position: absolute; left: 27px; top: 0; bottom: 0; width: 1px; background: rgba(0,0,0,.25); }
  .folder .brand { position: absolute; left: 0; right: 0; top: 88px; justify-content: center; }
  .folder .brand-name { font-size: 19px; }
  .folder .brand-tag { font-size: 5.5px; }
  .folder-url { position: absolute; left: 0; right: 0; top: 500px; text-align: center; color: #fff; font-size: 8px; letter-spacing: .03em; }

  /* letterhead */
  .letterhead { left: 615px; top: 95px; width: 403px; height: 522px; background: var(--paper); }
  .letterhead .brand { position: absolute; left: 37px; top: 36px; }
  .letterhead .brand-name { font-size: 13px; }
  .letterhead .brand-tag { font-size: 4.2px; }
  .contact { position: absolute; left: 292px; top: 30px; font-size: 5.2px; line-height: 7.4px; color: var(--muted); }
  .contact-row { display: flex; align-items: center; gap: 3px; }
  .icon { width: 5px; height: 5px; flex: none; }
  .contact-address { margin-top: 4px; }
  .letter { position: absolute; left: 37px; top: 154px; width: 330px; font-size: 5.6px; line-height: 7.1px; color: var(--ink); text-align: justify; }
  .letter p { margin-bottom: 7px; }
  .salutation { font-weight: bold; }
  .signoff { margin-top: 12px; font-size: 5.6px; line-height: 7.1px; }
  .signoff strong { color: var(--navy-deep); }
  .signature { position: absolute; left: 83px; top: 316px; width: 80px; height: 42px; background: linear-gradient(120deg, #e6e9f2, #dde2ef); border-radius: 3px; }

  .band { position: absolute; left: 0; bottom: 0; width: 100%; display: block; }

  /* envelope front */
  .envelope-front { left: 132px; top: 645px; width: 451px; height: 195px; background: var(--paper); }
  .envelope-front .brand { position: absolute; left: 20px; top: 20px; }
  .envelope-front .brand-name { font-size: 14px; }
  .envelope-front .brand-tag { font-size: 4.4px; }
  .envelope-address { position: absolute; left: 19px; top: 168px; font-size: 5.4px; line-height: 7px; color: var(--muted); }

  /* envelope back */
  .envelope-back { left: 615px; top: 645px; width: 451px; height: 195px; background: var(--paper); }
  .flap { position: absolute; left: 0; top: 0; width: 451px; height: 64px; display: block; }
  .envelope-url { position: absolute; left: 0; right: 0; top: 169px; text-align: center; font-size: 5.6px; color: var(--muted); }

  /* business cards */
  .card-front { left: 416px; top: 870px; width: 167px; height: 96px; background: var(--navy); }
  .card-front .brand { position: absolute; left: 0; right: 0; top: 36px; justify-content: center; gap: 4px; }
  .card-front .brand-mark { width: 9px; height: 9px; }
  .card-front .brand-name { font-size: 9.5px; }
  .card-front .brand-tag { font-size: 3px; margin-top: 2px; }
  .card-url { position: absolute; left: 0; right: 0; top: 80px; text-align: center; color: #fff; font-size: 4.2px; }

  .card-back { left: 615px; top: 870px; width: 167px; height: 96px; background: var(--paper); }
  .card-back .brand { position: absolute; left: 78px; top: 14px; gap: 4px; }
  .card-back .brand-mark { width: 8px; height: 8px; }
  .card-back .brand-name { font-size: 8px; }
  .card-back .brand-tag { font-size: 2.6px; margin-top: 2px; }
  .holder { position: absolute; left: 12px; top: 24px; }
  .holder-name { font-size: 5px; font-weight: bold; color: var(--navy); text-transform: uppercase; letter-spacing: .02em; }
  .holder-role { font-size: 3.8px; color: var(--muted); margin-top: 1px; }
  .card-contact { position: absolute; left: 12px; top: 62px; font-size: 3.6px; line-height: 5.3px; color: var(--muted); }
  .card-contact .icon { width: 3.6px; height: 3.6px; }
  .card-contact .contact-row { gap: 2px; }
  .card-address { position: absolute; right: 12px; top: 73px; font-size: 3.6px; line-height: 5.3px; color: var(--muted); text-align: right; }
</style>
</head>
<body>

<svg width="0" height="0" style="position:absolute" aria-hidden="true">
  <defs>
    <symbol id="icon-phone" viewBox="0 0 10 10"><rect width="10" height="10" rx="1.5" fill="#c0232b"/><path d="M3 2.2l1.2 1.6-.7.8c.5 1 1.2 1.7 2.2 2.2l.8-.7 1.6 1.2-.7 1c-2.6-.4-4.6-2.4-5-5z" fill="#fff"/></symbol>
    <symbol id="icon-fax" viewBox="0 0 10 10"><rect width="10" height="10" rx="1.5" fill="#c0232b"/><rect x="2.2" y="4" width="5.6" height="3.4" fill="#fff"/><rect x="3.2" y="2.2" width="3.6" height="1.4" fill="#fff"/></symbol>
    <symbol id="icon-mail" viewBox="0 0 10 10"><rect width="10" height="10" rx="1.5" fill="#c0232b"/><rect x="2" y="3" width="6" height="4" fill="#fff"/><path d="M2 3l3 2.2L8 3" stroke="#c0232b" stroke-width=".7" fill="none"/></symbol>
    <symbol id="icon-web" viewBox="0 0 10 10"><rect width="10" height="10" rx="1.5" fill="#c0232b"/><circle cx="5" cy="5" r="2.8" fill="none" stroke="#fff" stroke-width=".8"/><path d="M2.2 5h5.6M5 2.2v5.6" stroke="#fff" stroke-width=".6"/></symbol>
  </defs>
</svg>

<!-- Presentation folder -->
<section class="piece folder on-dark">
  <div class="folder-spine"></div>
  <div class="brand">
    <span class="brand-mark"></span>
    <div class="brand-text">
      <span class="brand-name">Corrindale Planners, LLC</span>
      <span class="brand-tag">Financial Planning and Consulting</span>
    </div>
  </div>
  <div class="folder-url">www.corrindaleplan.com</div>
</section>

<!-- Letterhead -->
<section class="piece letterhead">
  <div class="brand">
    <span class="brand-mark"></span>
    <div class="brand-text">
      <span class="brand-name">Corrindale Planners, LLC</span>
      <span class="brand-tag">Financial Planning and Consulting</span>
    </div>
  </div>
  <div class="contact">
    <div class="contact-row"><svg class="icon"><use href="#icon-phone"/></svg>555.014.2260</div>
    <div class="contact-row"><svg class="icon"><use href="#icon-fax"/></svg>555.014.2270</div>
    <div class="contact-row"><svg class="icon"><use href="#icon-web"/></svg>www.corrindaleplan.com</div>
    <div class="contact-address">418 Harlow Ave, Suite B<br>Brenton CA 90417</div>
  </div>
  <div class="letter">
    <p class="salutation">Dear sir,</p>
    <p>Thank you for your interest in Corrindale Planners. We help individuals, families and growing businesses build a clear picture of where they stand today and where they want to be tomorrow. Every plan we prepare begins with careful listening, because good advice depends on understanding the people it is meant to serve.</p>
    <p>Our advisors review savings, investments, insurance, tax matters and retirement goals together, so that each decision supports the others. We explain our reasoning in plain language and provide written summaries after every meeting. Clients receive regular reviews throughout the year, and we adjust recommendations as markets, laws and personal circumstances change. Our consulting services also assist small companies with budgeting, cash flow planning and employee benefit programs.</p>
    <p>We would welcome the opportunity to meet with you and discuss how our approach may fit your needs. An initial consultation carries no obligation and can be arranged at our office or by phone at a time that suits you.</p>
    <p>Please feel free to contact us with any questions. We look forward to hearing from you and to working together on a plan built for the years ahead.</p>
    <div class="signoff">Yours Sincerely,<br><strong>Dana Prescott</strong></div>
  </div>
  <div class="signature" role="img" aria-label="Handwritten signature"></div>
  <svg class="band" height="5" viewBox="0 0 403 5" preserveAspectRatio="none" aria-hidden="true">
    <polygon points="0,0 268,0 264,5 0,5" fill="var(--navy)"/>
    <polygon points="272,0 403,0 403,5 266,5" fill="var(--red)"/>
  </svg>
</section>

<!-- Envelope front -->
<section class="piece envelope-front">
  <div class="brand">
    <span class="brand-mark"></span>
    <div class="brand-text">
      <span class="brand-name">Corrindale Planners, LLC</span>
      <span class="brand-tag">Financial Planning and Consulting</span>
    </div>
  </div>
  <div class="envelope-address">418 Harlow Ave, Suite B<br>Brenton CA 90417</div>
  <svg class="band" height="6" viewBox="0 0 451 6" preserveAspectRatio="none" aria-hidden="true">
    <polygon points="0,0 314,0 309,6 0,6" fill="var(--navy)"/>
    <polygon points="320,0 451,0 451,6 313,6" fill="var(--red)"/>
  </svg>
</section>

<!-- Envelope back -->
<section class="piece envelope-back">
  <svg class="flap" viewBox="0 0 451 64" aria-hidden="true">
    <path d="M0,0 H451 L432,58 Q430,64 424,64 H27 Q21,64 19,58 Z" fill="var(--navy)"/>
  </svg>
  <div class="envelope-url">www.corrindaleplan.com</div>
</section>

<!-- Business card front -->
<section class="piece card-front on-dark">
  <div class="brand">
    <span class="brand-mark"></span>
    <div class="brand-text">
      <span class="brand-name">Corrindale Planners, LLC</span>
      <span class="brand-tag">Financial Planning and Consulting</span>
    </div>
  </div>
  <div class="card-url">www.corrindaleplan.com</div>
</section>

<!-- Business card back -->
<section class="piece card-back">
  <div class="holder">
    <div class="holder-name">Jordan Whitley</div>
    <div class="holder-role">General Manager</div>
  </div>
  <div class="brand">
    <span class="brand-mark"></span>
    <div class="brand-text">
      <span class="brand-name">Corrindale</span>
      <span class="brand-tag">Planners, LLC</span>
    </div>
  </div>
  <div class="card-contact">
    <div class="contact-row"><svg class="icon"><use href="#icon-phone"/></svg>555.014.2260</div>
    <div class="contact-row"><svg class="icon"><use href="#icon-fax"/></svg>555.014.2270</div>
    <div class="contact-row"><svg class="icon"><use href="#icon-mail"/></svg>info@corrindaleplan.com</div>
    <div class="contact-row"><svg class="icon"><use href="#icon-web"/></svg>www.corrindaleplan.com</div>
  </div>
  <div class="card-address">418 Harlow Ave, Suite B<br>Brenton CA 90417</div>
  <svg class="band" height="4" viewBox="0 0 167 4" preserveAspectRatio="none" aria-hidden="true">
    <polygon points="0,0 94,0 91,4 0,4" fill="var(--navy)"/>
    <polygon points="97,0 167,0 167,4 93,4" fill="var(--red)"/>
  </svg>
</section>

</body>
</html>
```